Town Planning Consultants require lstationary design

Require a design to be used for our letterhead and report cover page. We have an approved logo.
we have attached our logo, and our temporary letterhead/cover page (SEE Cover) which we currently adapt for both purposes in the interim pending a permanent design. I have also attached an example (example report cover) of a report cover page that I like. perhaps similar with our colour scheme

Target Market(s)

?

Industry/Entity Type

Town

Colors
249fd4
3176b5

Requirements
Must have
• colours to match logo
• the text content in existing letterhead

```html
<!DOCTYPE html>
<html lang="en">
<head>
<meta charset="utf-8">
<title>Calloway Urban – Report Cover and Letterhead</title>
<link href="https://fonts.googleapis.com/css2?family=Source+Sans+3:wght@400;600;700&display=swap" rel="stylesheet">
<style>
  :root {
    --brand-blue: #2fa5d9;
    --backdrop: #c9c9c9;
    --paper: #e6e6e6;
    --band-grey: #acacac;
    --ink: #1e1e1e;
    --rule: #8a8a8a;
    --white: #f4f4f4;
  }
  * { margin: 0; padding: 0; box-sizing: border-box; }
  html, body { width: 1200px; height: 857px; overflow: hidden; }
  body {
    background: var(--backdrop);
    font-family: "Source Sans 3", "Myriad Pro", Arial, sans-serif;
    color: var(--ink);
    position: relative;
  }
  .sheet {
    position: absolute;
    top: 53px;
    width: 526px;
    height: 746px;
    background: var(--paper);
    box-shadow: 1px 1px 2px rgba(0,0,0,0.18);
    overflow: hidden;
  }
  .sheet--cover { left: 60px; }
  .sheet--letterhead { left: 614px; top: 56px; height: 743px; }

  .wordmark {
    position: absolute;
    left: 0; right: 0;
    text-align: center;
    color: var(--brand-blue);
    font-weight: 600;
    letter-spacing: -0.5px;
    white-space: nowrap;
  }
  .sheet--cover .wordmark { top: 175px; font-size: 62px; }
  .sheet--letterhead .wordmark { top: 60px; font-size: 34px; left: 10px; }

  .report-title {
    position: absolute;
    top: 340px;
    left: 0; right: 0;
    text-align: center;
    color: var(--brand-blue);
    font-weight: 700;
    font-size: 41px;
    line-height: 42px;
  }
  .report-subtitle {
    position: absolute;
    top: 426px;
    left: 45px;
    width: 425px;
    border-top: 1px solid var(--rule);
    border-bottom: 1px solid var(--rule);
    padding: 3px 0 2px;
    text-align: center;
    font-size: 13px;
    font-weight: 600;
    letter-spacing: 3.1px;
    white-space: nowrap;
  }

  .credits {
    position: absolute;
    font-size: 12.5px;
    line-height: 18px;
  }
  .credits--prepared { left: 38px; top: 610px; }
  .credits--reviewed { right: 58px; top: 615px; text-align: right; }

  .footer-block {
    position: absolute;
    bottom: 0;
    left: 0;
    width: 168px;
    height: 85px;
    background: var(--brand-blue);
  }
  .footer-band {
    position: absolute;
    bottom: 0;
    left: 168px;
    right: 0;
    height: 49px;
    background: var(--band-grey);
  }
  .services {
    position: absolute;
    right: 43px;
    top: 5px;
    text-align: right;
    color: var(--white);
    font-weight: 700;
    font-size: 14.5px;
    line-height: 18px;
    letter-spacing: 0.5px;
  }
  .contact {
    position: absolute;
    left: 0; right: 0;
    top: 11px;
    text-align: center;
    color: var(--white);
    font-size: 8.6px;
    line-height: 16px;
  }
  .contact b { font-weight: 700; }
</style>
</head>
<body>

  <section class="sheet sheet--cover" aria-label="Report cover page">
    <div class="wordmark">Calloway Urban</div>

    <h1 class="report-title">Statement of<br>Environmental Effects</h1>
    <p class="report-subtitle">PROPOSED ADDITIONS TO EXISTING DWELLING</p>

    <div class="credits credits--prepared">
      <p>Prepared for: R.Hallett</p>
      <p>Prepared by: M.Tran</p>
    </div>
    <div class="credits credits--reviewed">
      <p>Reviewed by: P. Lindqvist</p>
      <p>Dated: June, 2016</p>
    </div>

    <div class="footer-block"></div>
    <footer class="footer-band">
      <p class="services">PLANNING | DEVELOPMENT<br>URBAN DESIGN | CONSULTANTS</p>
    </footer>
  </section>

  <section class="sheet sheet--letterhead" aria-label="Letterhead">
    <div class="wordmark">Calloway Urban</div>

    <div class="footer-block"></div>
    <footer class="footer-band">
      <p class="contact">
        12 Ridgeline Road, BANGALOW NSW 2479 &nbsp;|&nbsp; <b>P :</b> +61 (2) 6600 1234<br>
        <b>C :</b>+61 (0)400 555 018 &nbsp;<b>E :</b> info@callowayurban.com.au &nbsp;<b>W :</b> www.callowayurban.com.au
      </p>
    </footer>
  </section>

</body>
</html>
```